professional coaching community needs new look for website

We require a website design that attracts professionals. We run a large, global professional coaching community (e.g. executive, business, personal coaches NOT sports coaches). Our members are committed to their professional and personal development and they enjoy building relationships with other coaches across the world. We also champion the success of coaches and the coaching industry by providing business support resources to our members. We do not mind which colours you use, but whatever the combination, the combinations must be professional and refined. It would be good to have some of the familiarity of the old site colours, with some new, more professional element. We have a number of requirements for the homepage and members design, and this is attached.

Reason: I am extending the deadline for this design, in order to give feedback and see how current designs can be tweaked.

Target Market(s)

Here are some ideas for images, which gives and idea of the target market also:

Ideas for website images:

1. http://www.pixelvarno.com/stock-photo-48213077-business-success.php?st=4b2a918 (I like the people in this one – they seem very dynamic and a good mix of women and men)
2. http://www.pixelvarno.com/stock-photo-51729406-business-communications.php?st=4b2a918 (I like all of the speech bubbles in this one, that’s what the MentraLoop community does – pairs up in two’s or small groups and engages in professional talking)
3. http://www.pixelvarno.com/stock-photo-37086152-global-business-working.php?st=4b2a918 (I like the combination of the world and the people talking in different groups)
4. http://www.pixelvarno.com/stock-photo-44861039-global-business-people.php?st=e512604 (I like the world in this one – would be good to see combination of world and #1 dynamic people, which is the MentraLoop community)

Industry/Entity Type

Building

Requirements
Must have
• See attached uploaded files including homepage design, member dashboard design, and example profile (profiles need to be included him banner design). Note that any text must not be build into graphic. It needs to be able to be edited via html.

```html
<!DOCTYPE html>
<html lang="en">
<head>
<meta charset="utf-8">
<title>MentraLoop — Coaching Community</title>
<link rel="stylesheet" href="https://fonts.googleapis.com/css2?family=Lato:wght@400;700&family=Open+Sans:wght@400;600&display=swap">
<style>
:root{
  --navy:#1f3f73;
  --navy-dark:#1a3563;
  --green:#6cbd6a;
  --green-dark:#4fa24f;
  --text:#2b2b2b;
  --muted:#777;
  --line:#d9d9d9;
  --hero-bg:#f3f3f3;
  --footer:#3a3a3a;
  --footer-bottom:#2f2f2f;
  --footer-text:#9a9a9a;
  --red:#c0271f;
}
*{box-sizing:border-box;margin:0;padding:0}
html,body{width:895px;height:1200px;overflow:hidden;background:#fff}
body{font-family:"Open Sans",Arial,sans-serif;color:var(--text);position:relative}
.abs{position:absolute}
.heading{font-family:"Lato",Arial,sans-serif}

/* header */
.site-header{position:absolute;left:0;top:0;width:895px;height:48px;background:linear-gradient(#fff,#f7f7f7);box-shadow:0 2px 4px rgba(0,0,0,.12);z-index:2}
.brand{left:102px;top:8px;font-family:"Lato",sans-serif;font-weight:700;font-size:23px;color:var(--navy);letter-spacing:-.3px}
.main-nav a{position:absolute;top:25px;font-size:12px;color:#333;text-decoration:none}
.main-nav .active::after{content:"";position:absolute;left:-9px;right:-9px;top:20px;height:3px;background:var(--green)}
.lang{left:713px;top:0;width:71px;height:15px;background:#eee;border:1px solid #ddd;border-top:0;border-radius:0 0 3px 3px;font-size:8px;color:#888;padding:2px 0 0 22px}
.lang::before{content:"";position:absolute;left:7px;top:4px;width:10px;height:7px;background:#2a4d8f}
.btn{background:var(--navy);color:#fff;border-radius:2px;font-weight:600;text-align:center}
.login{left:723px;top:22px;width:51px;height:18px;font-size:9px;line-height:18px}

/* hero */
.hero{left:0;top:48px;width:895px;height:282px;background:var(--hero-bg)}
.hero-photo{left:380px;top:48px;width:450px;height:282px;background:radial-gradient(ellipse at 50% 40%,#dfe4ea 0%,#eceef1 45%,var(--hero-bg) 75%)}
.hero-title{left:102px;top:133px;font-size:24px;line-height:29px;color:var(--navy);font-weight:700}
.hero-btn{left:102px;top:212px;width:128px;height:24px;line-height:24px;font-size:12.5px;font-weight:400}
.below-hero{left:0;top:330px;width:895px;height:180px;background:linear-gradient(#eeeeee,#fff)}

/* benefits */
.benefits{left:106px;top:348px;width:453px;height:128px;background:#fff;border:1px solid var(--line)}
.panel-head{height:28px;border-bottom:1px solid var(--line);background:linear-gradient(#fff,#f1f1f1);text-align:center;font-family:"Lato",sans-serif;font-size:15px;line-height:28px;color:var(--navy)}
.benefit-list{position:absolute;list-style:none;font-size:11px;font-weight:600}
.benefit-list li{height:21px;padding-left:9px;position:relative}
.benefit-list li::before{content:"";position:absolute;left:0;top:6px;width:3px;height:3px;border-radius:50%;background:var(--green)}

/* video */
.video{left:106px;top:491px;width:453px;height:290px;background:#000;overflow:hidden}
.video-scene{left:0;top:0;width:453px;height:266px;background:radial-gradient(ellipse at 50% 55%,#6a6258 0%,#2c2924 40%,#0a0a0a 75%)}
.video-title{left:7px;top:5px;font-size:9px;color:#eee}
.video-bar{left:0;top:266px;width:453px;height:24px;background:linear-gradient(#2a2a2a,#111)}
.progress{left:0;top:266px;width:453px;height:4px;background:#555}
.progress i{position:absolute;left:0;top:0;width:96px;height:4px;background:var(--red)}
.video-time{left:63px;top:277px;font-size:8px;color:#ddd}
.video-brand{left:393px;top:277px;font-size:8px;color:#bbb;font-weight:600}

/* article */
.article-head{left:115px;top:808px;font-size:15px;color:var(--navy)}
.article{left:115px;top:834px;width:444px;font-size:10.6px;line-height:19.5px;color:#222}
.article a{color:var(--navy);text-decoration:none}

/* sign in */
.signin{left:573px;top:347px;width:211px;height:341px;background:linear-gradient(#f3f8fd,#dfeaf6);box-shadow:0 3px 6px rgba(0,0,0,.15);border-radius:3px}
.signin-head{left:573px;top:347px;width:211px;height:36px}
.signin-title{left:573px;top:353px;width:211px;text-align:center;font-size:15px;font-weight:700;color:#fff}
.perk{position:absolute;left:598px;font-size:10px;line-height:11px;color:#222;width:150px}
.perk-tag{position:absolute;left:574px;width:18px;height:11px}
.signin-rule{left:582px;top:526px;width:194px;height:1px;background:#b8cde0}
.field-label{position:absolute;left:582px;font-size:9.5px;color:#222}
.field{position:absolute;left:637px;width:138px;height:20px;background:#fff;border:1px solid #c6d2de;border-radius:2px;font-size:8px;font-style:italic;color:#999;padding:4px 0 0 6px}
.check{left:583px;top:624px;width:10px;height:10px;border:1px solid #9fb3c7;background:#fff}
.terms{left:598px;top:625px;width:170px;font-size:8px;line-height:9px;color:var(--navy)}
.signup{left:643px;top:655px;width:72px;height:16px;line-height:16px;font-size:10px}

.adv{left:573px;top:707px;width:211px;height:74px;background:#b3b3b3;color:#8a8a8a;font-weight:700;font-size:14px;text-align:center;line-height:74px}

.social{position:absolute;top:794px;width:20px;height:20px;border-radius:50%;background:#c7c7c7}
.social.on{background:var(--green)}

/* supporters */
.supporters{left:574px;top:825px;width:210px;height:251px;background:#fff;border:1px solid var(--line);border-radius:3px}
.supporters .panel-head{text-align:left;padding-left:13px;font-size:14px;height:32px;line-height:32px}
.sponsor{position:absolute;left:0;width:208px;text-align:center;font-family:"Lato",sans-serif;font-weight:700;font-size:15px}
.sponsor-rule{position:absolute;left:10px;width:188px;height:1px;background:#e2e2e2}
.more{position:absolute;left:0;top:232px;width:208px;text-align:center;font-size:8px;color:var(--red)}

/* footer */
.footer{left:0;top:1086px;width:895px;height:86px;background:var(--footer)}
.notch{left:443px;top:1086px;width:0;height:0;border-left:7px solid transparent;border-right:7px solid transparent;border-top:7px solid #fff}
.foot-nav{position:absolute;top:1111px;font-size:7px;color:var(--footer-text);letter-spacing:.2px}
.foot-nav.on{color:var(--green)}
.foot-sep{position:absolute;top:1110px;width:1px;height:10px;background:#555}
.foot-rule{left:119px;top:1129px;width:490px;height:1px;background:#4a4a4a}
.foot-rule.r{left:623px;width:154px}
.contact{position:absolute;top:1139px;font-size:8px;color:var(--footer-text)}
.ficon{position:absolute;top:1140px;width:10px;height:10px;border-radius:2px;background:#6f6f6f}
.footer-bottom{left:0;top:1172px;width:895px;height:28px;background:var(--footer-bottom)}
.legal{position:absolute;top:1183px;font-size:7.5px;color:#8d8d8d}
</style>
</head>
<body>

<header class="site-header">
  <div class="abs brand">MentraLoop</div>
  <nav class="main-nav">
    <a class="active" href="#" style="left:331px">Home</a>
    <a href="#" style="left:383px">Join Us</a>
    <a href="#" style="left:440px">Coaching</a>
    <a href="#" style="left:507px">Mentoring</a>
    <a href="#" style="left:581px">Supervision</a>
    <a href="#" style="left:659px">Resources</a>
  </nav>
  <div class="abs lang">English ▾</div>
  <div class="abs btn login">Login</div>
</header>

<section>
  <div class="abs hero"></div>
  <div class="abs hero-photo" role="img" aria-label="Group of business professionals standing in front of a faint world map"></div>
  <h1 class="abs heading hero-title">Join the most dinamic coaching<br>community in the world</h1>
  <div class="abs btn hero-btn">Connect with Coach</div>
  <div class="abs below-hero"></div>
</section>

<section class="abs benefits">
  <div class="panel-head">Why are there XXXX MentraLoops?</div>
  <ul class="benefit-list" style="left:19px;top:53px"><li>Benefit 1</li><li>Benefit 2</li><li>Benefit 3</li></ul>
  <ul class="benefit-list" style="left:174px;top:53px"><li>Benefit 1</li><li>Benefit 2</li><li>Benefit 3</li></ul>
  <ul class="benefit-list" style="left:329px;top:53px"><li>Benefit 1</li><li>Benefit 2</li><li>Benefit 3</li></ul>
</section>

<section class="abs video">
  <div class="abs video-scene" role="img" aria-label="Video still of a chess king piece on a board"></div>
  <div class="abs video-title">2013 ClipStage Player PSD</div>
  <svg class="abs" style="left:200px;top:128px" width="50" height="50" viewBox="0 0 50 50">
    <circle cx="25" cy="25" r="22" fill="rgba(0,0,0,.45)"/>
    <path d="M19 15 L35 25 L19 35 Z" fill="#fff"/>
  </svg>
  <div class="abs video-bar"></div>
  <div class="abs progress"><i></i></div>
  <svg class="abs" style="left:15px;top:275px" width="40" height="10" viewBox="0 0 40 10">
    <path d="M0 0 L8 5 L0 10 Z" fill="#ccc"/>
    <path d="M27 3 h3 l4-3 v10 l-4-3 h-3 Z" fill="#ccc"/>
  </svg>
  <div class="abs video-time">0:42 / 3:20</div>
  <div class="abs video-brand">Clip</div>
  <svg class="abs" style="left:430px;top:275px" width="11" height="11" viewBox="0 0 11 11" fill="none" stroke="#ccc" stroke-width="1.5">
    <path d="M0 3V0h3M8 0h3v3M11 8v3H8M3 11H0V8"/>
  </svg>
</section>

<article>
  <h2 class="abs heading article-head" style="font-weight:400">Not Too Long Header</h2>
  <p class="abs article">Lorem ipsum dolor sit amet, consectetuer adipiscing elit. Aenean commodo ligula eget dolor. Aenean massa. Cum sociis natoque penatibus et magnis dis parturient montes, nascetur ridiculus mus. Donec quam felis, ultricies nec, pellentesque eu, pretium quis, sem. Nulla consequat massa quis enim. Donec pede justo, fringilla vel, aliquet nec, vulputate eget, arcu. In enim justo, rhoncus ut, imperdiet a, venenatis vitae, justo. Nullam dictum felis eu pede mollis pretium. Integer tincidunt. Cras dapibus.<br><a href="#">Vivamus elementum semper nisi.</a> Aenean vulputate eleifend tellus. Aenean leo ligula, porttitor eu, consequat vitae, eleifend ac, enim. Aliquam lorem ante, dapibus in, viverra quis, feugiat a, tellus. Phasellus viverra nulla ut metus varius laoreet. Quisque rutrum. Aenean imperdiet. Etiam ultricies nisi vel augue. Curabitur ullamcorper ultricies nisi. Nam eget dui.</p>
</article>

<aside>
  <div class="abs signin"></div>
  <svg class="abs signin-head" width="211" height="36" viewBox="0 0 211 36">
    <path d="M0 3 Q0 0 3 0 H208 Q211 0 211 3 V28 L105 36 L0 28 Z" fill="var(--green)"/>
  </svg>
  <div class="abs heading signin-title">Quick Sign In</div>

  <svg class="perk-tag" style="top:398px" viewBox="0 0 18 11"><path d="M0 0H12L18 5.5L12 11H0Z" fill="var(--green)"/></svg>
  <div class="perk" style="top:399px">Free to join</div>
  <svg class="perk-tag" style="top:424px" viewBox="0 0 18 11"><path d="M0 0H12L18 5.5L12 11H0Z" fill="var(--green)"/></svg>
  <div class="perk" style="top:420px">3 issues of Coaching Research in Practice</div>
  <svg class="perk-tag" style="top:451px" viewBox="0 0 18 11"><path d="M0 0H12L18 5.5L12 11H0Z" fill="var(--green)"/></svg>
  <div class="perk" style="top:447px">Monthly issues of Lessons from the Field</div>
  <svg class="perk-tag" style="top:475px" viewBox="0 0 18 11"><path d="M0 0H12L18 5.5L12 11H0Z" fill="var(--green)"/></svg>
  <div class="perk" style="top:476px">Access to our community</div>
  <svg class="perk-tag" style="top:499px" viewBox="0 0 18 11"><path d="M0 0H12L18 5.5L12 11H0Z" fill="var(--green)"/></svg>
  <div class="perk" style="top:500px">Online profile</div>

  <div class="abs signin-rule"></div>
  <div class="field-label" style="top:540px">First Name:</div>
  <div class="field" style="top:535px">Your name</div>
  <div class="field-label" style="top:571px">Last Name:</div>
  <div class="field" style="top:566px">Your name</div>
  <div class="field-label" style="top:600px">Email:</div>
  <div class="field" style="top:595px">Your name</div>
  <div class="abs check"></div>
  <div class="abs terms">I have read the MentraLoop Terms and Conditions</div>
  <div class="abs btn signup">Sign Up Now</div>

  <div class="abs adv">Adv</div>

  <span class="social" style="left:576px"></span>
  <span class="social on" style="left:604px"></span>
  <span class="social" style="left:631px"></span>
  <span class="social" style="left:658px"></span>

  <section class="abs supporters">
    <div class="panel-head">Thanks to our Supporters</div>
    <div class="sponsor" style="top:57px;color:#f05a22">Swiftmark</div>
    <div class="sponsor-rule" style="top:98px"></div>
    <div class="sponsor" style="top:117px;color:var(--navy)">Hemline</div>
    <div class="sponsor-rule" style="top:158px"></div>
    <div class="sponsor" style="top:179px;color:#e8452c">Orbipay</div>
    <div class="more">See more of our supporters »</div>
  </section>
</aside>

<footer>
  <div class="abs footer"></div>
  <div class="abs notch"></div>
  <span class="foot-nav" style="left:120px">HOME</span>
  <span class="foot-sep" style="left:151px"></span>
  <span class="foot-nav on" style="left:166px">FEATURES</span>
  <span class="foot-sep" style="left:211px"></span>
  <span class="foot-nav" style="left:224px">BLOG</span>
  <span class="foot-sep" style="left:256px"></span>
  <span class="foot-nav" style="left:269px">PORTFOLIO</span>
  <span class="foot-sep" style="left:318px"></span>
  <span class="foot-nav" style="left:332px">CONTACT</span>
  <span class="foot-nav" style="left:623px">STAY CONNECTED</span>
  <div class="abs foot-rule"></div>
  <div class="abs foot-rule r"></div>

  <svg class="abs" style="left:120px;top:1137px" width="11" height="10" viewBox="0 0 11 10"><path d="M5.5 0L11 5H9.5V10H1.5V5H0Z" fill="#777"/></svg>
  <span class="contact" style="left:135px">48 Alder Row, Brookvale, NV, 89012, USA</span>
  <svg class="abs" style="left:320px;top:1138px" width="10" height="10" viewBox="0 0 10 10"><path d="M2 0L4 2.5L2.8 3.8Q4 6.5 6.2 7.2L7.5 6L10 8L8.5 10Q2 9 0 1.5Z" fill="#777"/></svg>
  <span class="contact" style="left:335px">(555) 318-2046</span>
  <svg class="abs" style="left:418px;top:1139px" width="11" height="8" viewBox="0 0 11 8"><rect width="11" height="8" fill="#777"/><path d="M0 0L5.5 4.5L11 0" stroke="#3a3a3a" fill="none"/></svg>
  <span class="contact" style="left:435px">hello@mentraloop.net</span>

  <span class="ficon" style="left:626px"></span>
  <span class="ficon" style="left:651px"></span>
  <span class="ficon" style="left:675px"></span>
  <span class="ficon" style="left:700px;background:var(--green)"></span>
  <span class="ficon" style="left:724px"></span>
  <span class="ficon" style="left:748px;border-radius:50%"></span>

  <div class="abs footer-bottom"></div>
  <span class="legal" style="left:119px">Mentra © 2013</span>
  <span class="legal" style="left:191px;color:#555">|</span>
  <span class="legal" style="left:202px">Legal Notice</span>
  <span class="legal" style="left:256px;color:#555">|</span>
  <span class="legal" style="left:265px">Terms</span>
</footer>

</body>
</html>
```